Plakat-Design für ein großes, geistliches Konzert für Chor, Orchester und Solisten
Zielgruppe
Wir sind eine Kantorei einer Kirchengemeinde, die in jedem Jahr ein großes Konzert für Chor, Orchester und Solisten veranstaltet. In diesem Jahr ist das Konzert in doppeltem Sinn etwas Besonderes. Zum einen weil wir das Konzert in Kooperation mit einer anderen Kantorei bestreiten und zum anderen weil die Anzahl der Mitwirkenden so groß ist, dass wir nicht der Kirche sondern das Konzert in die hiesige Stadthalle verlagern. Die Kirchenmusik präsentiert sozusagen sich außerhalb ihrer eigenen Mauern.
Eine Zielgruppe sollen diejenigen sein, die sich durch den besoneren Veranstaltungsort ansprechen lassen, also eher kirchenfremde Menschen. Das Plakat sollte auch das bestehende Stammpublikum nicht abschrecken, sondern einladen.
Es ist ein Folgeauftrag geplant, und zwar ein Programmheft/Textheft für das Konzert mit dem gleichen Design als Grundlage.
Aufgabenstellung
Das Plakat soll im DIN A3 oder A4 Hochformat erstellt werden.
Zwei weitere Logos von Förderern folgen noch.
Außer der Turm sind alle Logos von Förderern.
Der Turm ist sozusagen unser Markenzeichen und ein Wiedererkennungsmerkmal.
Das Konzert steht unter dem Motto: Von der Finsternis zum Licht.
Bezüglich der Textgröße sollte dieses Motto nicht größer sein als z.B. der Komponist und das Werk. Vielmehr soll das Motto durch ein grafisches Element eingearbeitet werden. 'Brautigorff' und 'Sternruf' sollen Eye catcher-Worte sein. Sternruf ist der Titel des Konzertes!

```html
<!DOCTYPE html>
<html lang="de">
<head>
<meta charset="utf-8">
<title>Von der Finsternis zum Licht – Konzertplakat</title>
<link rel="stylesheet" href="https://fonts.googleapis.com/css2?family=Alfa+Slab+One&family=Roboto:wght@400;500&display=swap">
<style>
  :root {
    --gold-dark: #b88a2a;
    --gold: #e0a400;
    --gold-light: #e6c26a;
    --text-gold: #ecd08a;
    --black: #000000;
    --magenta: #a8177f;
    --band-grey: #3a3a3e;
    --white: #ffffff;
    --muted: #9a9a9a;
    --ink: #1a1a1a;
  }
  html, body { margin: 0; padding: 0; overflow: hidden; background: var(--white); }
  .poster {
    position: relative; width: 849px; height: 1200px; overflow: hidden;
    background: var(--black); font-family: "Roboto", Arial, sans-serif;
  }
  .motto-band {
    position: absolute; left: 0; top: 0; width: 100%; height: 60px;
    background: linear-gradient(90deg, var(--gold-dark) 0%, var(--gold) 50%, var(--gold-light) 100%);
    display: flex; align-items: center; justify-content: center;
    font-size: 30px; letter-spacing: 1px; color: #111111; font-weight: 500;
  }
  .light-burst {
    position: absolute; left: 0; top: 340px; width: 100%; height: 700px;
    background: radial-gradient(circle at 50% 40%, #ffffff 0%, #fff3c4 5%, #f1c24e 14%, #9a6a12 32%, rgba(60,35,5,0.6) 50%, rgba(0,0,0,0) 70%);
  }
  .composer {
    position: absolute; left: 0; top: 90px; width: 100%; margin: 0;
    font-family: "Alfa Slab One", Georgia, serif; font-weight: 400;
    font-size: 76px; line-height: 82px; text-align: center;
    background: linear-gradient(90deg, var(--gold-dark), var(--gold) 55%, var(--gold-light));
    -webkit-background-clip: text; background-clip: text; color: transparent;
  }
  .composer .first-line { display: block; }
  .work-cantata {
    position: absolute; left: 0; top: 262px; width: 100%; text-align: center;
    font-size: 28px; color: var(--text-gold);
  }
  .work-title {
    position: absolute; left: 0; top: 302px; width: 100%; text-align: center;
    font-family: "Alfa Slab One", Georgia, serif; font-size: 46px;
    color: var(--gold);
  }
  .date-badge {
    position: absolute; left: 592px; top: 413px; width: 226px; height: 226px;
    border-radius: 50%; background: var(--magenta);
    display: flex; align-items: center; justify-content: center;
  }
  .date-text {
    display: block; margin: 0; transform: rotate(-5deg); text-align: center;
    color: var(--white); font-size: 18.5px; line-height: 28px; font-weight: 500;
  }
  .credits {
    position: absolute; left: 35px; top: 742px; margin: 0; padding: 0;
    list-style: none; color: var(--text-gold); font-size: 19px; line-height: 28.3px;
  }
  .prices {
    position: absolute; left: 35px; top: 960px; color: var(--text-gold);
    font-size: 19px; line-height: 28.5px;
  }
  .prices p { margin: 0; }
  .brand-mark {
    position: absolute; left: 700px; top: 880px; width: 120px;
    display: flex; align-items: center; gap: 6px;
    color: var(--white); font-size: 15px; font-weight: 500; line-height: 18px;
  }
  .brand-mark .dot { width: 10px; height: 10px; border-radius: 50%; background: var(--white); flex: none; }
  .info-band {
    position: absolute; left: 0; top: 1031px; width: 100%; height: 44px;
    background: var(--band-grey); color: var(--white); font-size: 15px;
  }
  .info-band span { position: absolute; top: 13px; white-space: nowrap; }
  .info-label { left: 22px; }
  .info-url-parish { left: 231px; }
  .info-url-society { left: 412px; }
  .info-url-hall { left: 625px; }
  .sponsors {
    position: absolute; left: 0; top: 1075px; width: 100%; height: 125px;
    background: var(--white);
  }
  .sponsors-label { position: absolute; left: 28px; top: 10px; font-size: 13.5px; color: var(--ink); }
  .sponsor-name {
    position: absolute; left: 72px; top: 58px; color: var(--magenta);
    font-size: 15px; font-weight: 500; letter-spacing: 1px;
  }
  .sponsor-placeholder {
    position: absolute; top: 36px; width: 160px; text-align: center;
    color: var(--muted); font-size: 24px; line-height: 31px;
  }
  .sponsor-two { left: 349px; }
  .sponsor-three { left: 622px; }
</style>
</head>
<body>
<div class="poster">
  <header class="motto-band">VON DER FINSTERNIS ZUM LICHT</header>

  <div class="light-burst" role="img" aria-label="Goldener Lichtstrahl mit funkelnden Partikeln auf schwarzem Grund"></div>

  <h1 class="composer"><span class="first-line">Anselm Brautigorff-</span>Kestrup:</h1>
  <div class="work-cantata">Choralkantate „Wer still dem hellen Morgen traut“</div>
  <div class="work-title">Sternruf-Sinfonie op. 37</div>

  <div class="date-badge">
    <p class="date-text">Sonntag,<br>22.09.2019<br>um 18.00 Uhr in<br>der Stadthalle Gilmsdorf<br>Einlass:<br>17.30 Uhr</p>
  </div>

  <ul class="credits">
    <li>Lena Morbach und Clara-Marie Hesse, Sopran</li>
    <li>Jonas Ellvik, Tenor</li>
    <li>Kammersymphonie Auental</li>
    <li>Kirchenkreiskantorei Wolfsmoor</li>
    <li>Kantorei St. Aegidien, Gilmsdorf</li>
    <li>Gesamtleitung: Kirchenkreiskantoren</li>
    <li>Tobias Rehlingen (WMO) und Simon Falkert (GD)</li>
  </ul>

  <div class="prices">
    <p>Eintrittspreise: 25,- / 20,- / 15,- Euro (Ermäßigungen 50%)</p>
    <p>Kartenvorverkauf: Kulturverein Gilmsdorf, Lindenweg 7, 29471 GD</p>
  </div>

  <div class="brand-mark"><span class="dot"></span><span>Kantorei St.&nbsp;Aegidien</span></div>

  <div class="info-band">
    <span class="info-label">Weitere Informationen unter :</span>
    <span class="info-url-parish">www.aegidien-gd.de</span>
    <span class="info-url-society">www.kulturverein-gd.de</span>
    <span class="info-url-hall">www.stadthalle-gd.de</span>
  </div>

  <footer class="sponsors">
    <div class="sponsors-label">Danke an unsere Förderer:</div>
    <div class="sponsor-name">Kirchenkreis Gilmsdorf</div>
    <div class="sponsor-placeholder sponsor-two">Logo<br>Förderer 2</div>
    <div class="sponsor-placeholder sponsor-three">Logo<br>Förderer 3</div>
  </footer>
</div>
</body>
</html>
```